Bluecrest Wellness Group Website

Need a informative, detailed and functional website for a medical cannabis clinic website

check out www.dumelvaclinic.com as competition - want better site than they have

Target Market(s)

Patients

Industry/Entity Type

Health Care

Number of Pages Required

1 page

Font styles to use
Sans Serif

Colors
cadf82
abd036
9bcb3b
3276b5
33a6d7
0392cd
f68d4e

Requirements
Must have
• Clean / Informative
• Will add additional educational content on opioid reduction
Nice to have
• like the white contrast with black/slate dividers. Green logo looks good on slate
• Check documents for ppt regarding website ideas
Should not have
• too many words

```html
<!DOCTYPE html>
<html lang="en">
<head>
<meta charset="utf-8">
<title>Bluecrest Wellness Group</title>
<link href="https://fonts.googleapis.com/css2?family=Montserrat:wght@400;600;700&family=Open+Sans:wght@400;600&display=swap" rel="stylesheet">
<style>
:root{
  --green:#8dc63f;
  --green-light:#abd036;
  --green-pale:#cadf82;
  --ink:#222222;
  --text:#555555;
  --grey-bg:#f3f3f3;
  --slate:#262626;
  --slate-deep:#161616;
  --white:#ffffff;
}
*{margin:0;padding:0;box-sizing:border-box}
html,body{width:1200px;height:4327px;overflow:hidden;background:var(--white)}
body{font-family:"Open Sans",Arial,sans-serif;color:var(--text);position:relative}
.section{position:absolute;left:0;width:1200px}
.abs{position:absolute}
.center{left:0;width:1200px;text-align:center}
h1,h2,h3,h4{font-family:"Montserrat",Arial,sans-serif;color:var(--ink)}
p{font-size:13px;line-height:24px}
.btn{position:absolute;display:flex;align-items:center;justify-content:center;background:var(--green);color:var(--white);border-radius:30px;font-family:"Montserrat",Arial,sans-serif;font-size:13px;font-weight:600}
.divider{position:absolute;left:560px;width:80px;height:20px}

/* top bar */
.topbar{top:0;height:35px;background:var(--green);color:var(--white);font-size:12px}
.topbar .item{position:absolute;top:9px;display:flex;align-items:center;gap:8px}
.topbar .social{position:absolute;top:10px;width:14px;height:14px;border-radius:50%;background:var(--white)}

/* header */
.header{top:35px;height:115px;background:var(--white)}
.brand{position:absolute;left:160px;top:22px;display:flex;align-items:center;gap:14px}
.brand-mark{width:62px;height:62px;border-radius:50%;background:var(--green)}
.brand-name{font-family:"Montserrat",Arial,sans-serif;font-size:16px;font-weight:600;letter-spacing:3px;line-height:20px;color:var(--green);text-transform:uppercase;border-left:2px solid var(--green);padding-left:12px}
.nav{position:absolute;top:48px;font-size:13px;color:var(--ink)}
.search{position:absolute;left:1018px;top:40px;width:34px;height:34px;border:2px solid var(--ink);border-radius:50%}

/* hero */
.hero{top:150px;height:623px;background:radial-gradient(ellipse at 48% 40%,#5c7a3c 0%,#2f4a23 45%,#16240f 100%)}
.hero .kicker{top:218px;font-size:15px;color:var(--white);letter-spacing:1px}
.hero h1{top:242px;font-size:40px;font-weight:700;color:var(--white)}
.hero p{top:315px;left:300px;width:600px;text-align:center;color:var(--white);font-size:13px}

/* feature boxes */
.features{top:701px;left:150px;width:906px;height:314px;display:flex}
.feature{width:302px;height:314px;background:var(--grey-bg);text-align:center;position:relative;border-right:1px solid #e4e4e4}
.feature.active{background:var(--green)}
.feature.active h3,.feature.active p{color:var(--white)}
.feature h3{margin-top:50px;font-size:18px;font-weight:700}
.feature .icon{position:absolute;left:111px;top:95px;width:80px;height:80px;border-radius:50%}
.feature p{position:absolute;left:38px;top:205px;width:226px;font-size:12px;line-height:22px}

/* about */
.about{top:1015px;height:456px}
.about h2{top:123px;font-size:32px;font-weight:700}
.about p{top:190px;left:150px;width:900px;text-align:center}

/* steps */
.steps{top:1471px;height:727px;background:var(--grey-bg)}
.steps h2{top:127px;font-size:22px;font-weight:700}
.steps .intro{top:175px;left:200px;width:800px;text-align:center}
.step{position:absolute;top:294px;width:280px;text-align:center}
.step .photo{width:180px;height:180px;border-radius:50%;margin:0 auto;border:6px solid var(--green);box-shadow:0 0 0 6px var(--white) inset}
.step .badge{position:absolute;left:190px;top:0;width:40px;height:40px;border-radius:50%;background:var(--slate)}
.step h4{margin-top:20px;font-size:15px;font-weight:700}
.step p{font-size:12px;line-height:20px;width:210px;margin:10px auto 0}
.step .btn{left:75px;top:338px;width:130px;height:36px;background:var(--green-pale);color:var(--ink);font-size:11px}

/* benefits */
.benefits{top:2198px;height:618px}
.benefits .plant{left:87px;top:38px;width:461px;height:548px;border-radius:40%;background:radial-gradient(circle at 50% 50%,#9ccf4e 0%,#5f9a2d 45%,rgba(95,154,45,0) 72%)}
.benefits .kicker{left:575px;top:82px;font-size:14px;letter-spacing:1px;color:var(--text)}
.benefits h2{left:575px;top:112px;font-size:33px;font-weight:700}
.benefit{position:absolute;width:200px}
.benefit .icon{width:50px;height:50px;border-radius:50%;background:var(--green)}
.benefit h4{font-size:15px;font-weight:700;margin-top:16px}
.benefit p{font-size:12px;line-height:21px;margin-top:8px}

/* doctor band */
.doctor{top:2816px;height:288px;background:linear-gradient(90deg,#2b2b2b 0%,#4a4a4a 45%,#6b6b6b 70%,#3a3a3a 100%)}
.doctor h2{top:108px;font-size:32px;font-weight:700;color:var(--white)}

/* network */
.network{top:3104px;height:641px}
.network h2{top:122px;font-size:22px;font-weight:700}
.network .intro{top:168px;left:200px;width:800px;text-align:center}
.card{position:absolute;top:271px;width:277px;height:318px;background:var(--grey-bg);text-align:center}
.card .photo{height:165px}
.card h4{margin-top:28px;font-size:14px;font-weight:700}
.card p{font-size:12px;line-height:20px;width:220px;margin:10px auto 0}

/* subscribe */
.subscribe{top:3745px;height:164px;background:#f7f7f7}
.subscribe .field{left:274px;top:55px;width:400px;height:54px;border-radius:30px;background:var(--white);box-shadow:0 2px 8px rgba(0,0,0,.08);font-size:13px;color:#aaa;padding:18px 0 0 28px}
.subscribe .btn{left:525px;top:55px;width:150px;height:54px;font-size:14px}
.subscribe .follow{left:695px;top:72px;font-size:15px;color:var(--ink)}
.subscribe .social{position:absolute;top:65px;width:36px;height:36px;border-radius:50%;background:var(--green)}

/* footer */
.footer{top:3909px;height:361px;background:linear-gradient(180deg,var(--slate) 0%,#1d261a 100%)}
.footer .brand{left:237px;top:70px}
.footer .brand-name{font-size:20px;line-height:24px}
.footer .brand-mark{width:76px;height:76px}
.footer .about-text{left:237px;top:168px;width:300px;color:#ddd;font-size:13px;line-height:22px}
.footer h4{position:absolute;top:62px;font-size:18px;font-weight:700;color:var(--white)}
.footer .links{position:absolute;left:563px;top:118px;list-style:none;color:#ddd;font-size:13px;line-height:29px}
.footer .links li::before{content:"›";margin-right:8px}
.footer .contact{position:absolute;left:776px;color:#ddd;font-size:13px;display:flex;align-items:center;gap:16px}
.copyright{top:4270px;height:57px;background:var(--slate-deep);color:#ccc;font-size:12px;text-align:center;line-height:57px}
</style>
</head>
<body>

<!-- top bar -->
<div class="section topbar">
  <div class="item" style="left:160px">
    <svg width="14" height="14" viewBox="0 0 24 24"><path fill="#fff" d="M6.6 10.8a15 15 0 0 0 6.6 6.6l2.2-2.2c.3-.3.7-.4 1-.2 1.1.4 2.3.6 3.6.6.6 0 1 .4 1 1V20c0 .6-.4 1-1 1A17 17 0 0 1 3 4c0-.6.4-1 1-1h3.5c.6 0 1 .4 1 1 0 1.3.2 2.5.6 3.6.1.3 0 .7-.2 1z"/></svg>
    <span>88-888-8888</span>
  </div>
  <div class="item" style="left:290px">
    <svg width="14" height="12" viewBox="0 0 24 18"><rect x="1" y="1" width="22" height="16" fill="none" stroke="#fff" stroke-width="2"/><path d="M1 1l11 9 11-9" fill="none" stroke="#fff" stroke-width="2"/></svg>
    <span>info@yourmail.com</span>
  </div>
  <span class="social" style="left:955px"></span>
  <span class="social" style="left:980px"></span>
  <span class="social" style="left:1005px"></span>
</div>

<!-- header -->
<header class="section header">
  <div class="brand">
    <span class="brand-mark"></span>
    <span class="brand-name">Bluecrest<br>Wellness<br>Group</span>
  </div>
  <span class="nav" style="left:430px">Home</span>
  <span class="nav" style="left:510px">About</span>
  <span class="nav" style="left:590px">Qualify</span>
  <span class="nav" style="left:678px">Appointments</span>
  <span class="nav" style="left:810px">FAQ</span>
  <span class="nav" style="left:878px">News</span>
  <span class="nav" style="left:950px">Contact</span>
  <span class="search"><svg width="30" height="30" viewBox="0 0 30 30"><circle cx="13" cy="13" r="5" fill="none" stroke="#222" stroke-width="2"/><path d="M17 17l4 4" stroke="#222" stroke-width="2"/></svg></span>
</header>

<!-- hero -->
<section class="section hero" role="img" aria-label="Photo of a smiling doctor holding a clipboard in a cannabis field">
  <div class="abs center kicker">WE HELP CANNABIS</div>
  <h1 class="abs center">BUSINESS GROW</h1>
  <p class="abs">Lorem ipsum dolor sit amet, consectetur adipiscing elit, sed do eiusmod tempor incididunt ut labore et dolore magna aliqua. Ut enim ad minim veniam, quis nostrud exercitation</p>
  <span class="btn" style="left:521px;top:407px;width:158px;height:44px">More Info</span>
</section>

<!-- feature boxes -->
<div class="section features">
  <div class="feature active">
    <h3>100% Risk Free</h3>
    <svg class="icon" viewBox="0 0 80 80"><circle cx="40" cy="40" r="38" fill="#fff"/><circle cx="40" cy="40" r="28" fill="none" stroke="#8dc63f" stroke-width="3"/><text x="40" y="44" text-anchor="middle" font-family="Montserrat,sans-serif" font-size="12" font-weight="700" fill="#222">100%</text></svg>
    <p>Lorem ipsum dolor sit amet, consectetur adipiscing elit, sed do eiusmod tempor incididunt ut labore</p>
  </div>
  <div class="feature">
    <h3>FREE Pre-Qualification</h3>
    <svg class="icon" viewBox="0 0 80 80"><circle cx="40" cy="40" r="38" fill="#8dc63f"/><rect x="28" y="24" width="22" height="30" rx="2" fill="none" stroke="#fff" stroke-width="2.5"/><path d="M33 33h12M33 40h12M33 47h7" stroke="#fff" stroke-width="2.5"/><path d="M44 52l4 4 8-9" fill="none" stroke="#fff" stroke-width="2.5"/></svg>
    <p>Lorem ipsum dolor sit amet, consectetur adipiscing elit, sed do eiusmod tempor incididunt ut labore</p>
  </div>
  <div class="feature">
    <h3>FAQ</h3>
    <svg class="icon" viewBox="0 0 80 80"><circle cx="40" cy="40" r="38" fill="#8dc63f"/><circle cx="40" cy="38" r="16" fill="none" stroke="#fff" stroke-width="2.5"/><path d="M34 34a6 6 0 1 1 8 5.5c-1.5.6-2 1.5-2 3" fill="none" stroke="#fff" stroke-width="2.5"/><circle cx="40" cy="47" r="1.8" fill="#fff"/></svg>
    <p>Lorem ipsum dolor sit amet, consectetur adipiscing elit, sed do eiusmod tempor incididunt ut labore</p>
  </div>
</div>

<!-- about -->
<section class="section about">
  <svg class="divider" style="top:75px" viewBox="0 0 80 20"><path d="M0 10h30M50 10h30" stroke="#8dc63f" stroke-width="1.5"/><circle cx="40" cy="10" r="6" fill="#8dc63f"/></svg>
  <h2 class="abs center">ABOUT US</h2>
  <p class="abs">Lorem ipsum dolor sit amet, consectetur adipiscing elit, sed do eiusmod tempor incididunt ut labore et dolore magna aliqua. Ut enim ad minim veniam, quis nostrud exercitation ullamco laboris nisi ut aliquip ex ea commodo consequat. Duis aute irure dolor in reprehenderit in voluptate velit esse cillum dolore eu fugiat nulla pariatur. Excepteur sint occaecat cupidatat non proident, sunt in culpa qui officia deserunt mollit anim id est laborum</p>
  <span class="btn" style="left:521px;top:341px;width:158px;height:44px">More Info</span>
</section>

<!-- steps -->
<section class="section steps">
  <svg class="divider" style="top:72px" viewBox="0 0 80 20"><path d="M0 10h30M50 10h30" stroke="#8dc63f" stroke-width="1.5"/><circle cx="40" cy="10" r="6" fill="#8dc63f"/></svg>
  <h2 class="abs center">3 Steps to Get Your Arkansas medical cannabis</h2>
  <p class="abs intro">Lorem ipsum dolor sit amet, consectetur adipiscing elit, sed do eiusmod tempor incididunt ut labore et dolore magna aliqua. Ut enim ad minim veniam, quis nostrud exercitation ullamco laboris nisi.</p>
  <svg class="abs" style="left:380px;top:380px" width="440" height="4"><path d="M0 2h440" stroke="#cadf82" stroke-width="2"/></svg>
  <div class="step" style="left:151px">
    <div class="photo" role="img" aria-label="Photo of a young cannabis seedling in soil" style="background:radial-gradient(circle,#4f8a2a 0%,#2d4a1c 55%,#3b2a1c 100%)"></div>
    <span class="badge"></span>
    <h4>Lorem ipsum dolor</h4>
    <p>Lorem ipsum dolor sit amet, consectetur adipiscing elit, sed do eiusmod tempor</p>
    <span class="btn">Book Appointment</span>
  </div>
  <div class="step" style="left:460px">
    <div class="photo" role="img" aria-label="Photo of a flowering cannabis plant close up" style="background:radial-gradient(circle,#a6cf5a 0%,#5f9a2d 55%,#2e4e1a 100%)"></div>
    <span class="badge"></span>
    <h4>Lorem ipsum dolor</h4>
    <p>Lorem ipsum dolor sit amet, consectetur adipiscing elit, sed do eiusmod tempor</p>
    <span class="btn">Book Appointment</span>
  </div>
  <div class="step" style="left:766px">
    <div class="photo" role="img" aria-label="Photo of dense green cannabis leaves" style="background:radial-gradient(circle,#7fbf3a 0%,#4c8a24 55%,#2a4a16 100%)"></div>
    <span class="badge"></span>
    <h4>Lorem ipsum dolor</h4>
    <p>Lorem ipsum dolor sit amet, consectetur adipiscing elit, sed do eiusmod tempor</p>
    <span class="btn">Book Appointment</span>
  </div>
</section>

<!-- benefits -->
<section class="section benefits">
  <div class="abs plant" role="img" aria-label="Photo of a potted cannabis plant seen from above"></div>
  <div class="abs kicker">BENEFITS YOU GET WITH</div>
  <h2 class="abs">Arkansas Medical Cannabis</h2>
  <div class="benefit" style="left:572px;top:188px">
    <svg class="icon" viewBox="0 0 50 50"><circle cx="25" cy="25" r="25" fill="#8dc63f"/><path d="M16 25l6 6 12-12" fill="none" stroke="#fff" stroke-width="3"/></svg>
    <h4>Lorem Ipsum</h4>
    <p>Lorem ipsum dolor sit amet, consectetur adipiscing elit, sed do eiusmod tempor</p>
  </div>
  <div class="benefit" style="left:826px;top:188px">
    <svg class="icon" viewBox="0 0 50 50"><circle cx="25" cy="25" r="25" fill="#8dc63f"/><path d="M16 25l6 6 12-12" fill="none" stroke="#fff" stroke-width="3"/></svg>
    <h4>Lorem Ipsum</h4>
    <p>Lorem ipsum dolor sit amet, consectetur adipiscing elit, sed do eiusmod tempor</p>
  </div>
  <div class="benefit" style="left:572px;top:387px">
    <svg class="icon" viewBox="0 0 50 50"><circle cx="25" cy="25" r="25" fill="#8dc63f"/><path d="M16 25l6 6 12-12" fill="none" stroke="#fff" stroke-width="3"/></svg>
    <h4>Lorem Ipsum</h4>
    <p>Lorem ipsum dolor sit amet, consectetur adipiscing elit, sed do eiusmod tempor</p>
  </div>
  <div class="benefit" style="left:826px;top:387px">
    <svg class="icon" viewBox="0 0 50 50"><circle cx="25" cy="25" r="25" fill="#8dc63f"/><path d="M16 25l6 6 12-12" fill="none" stroke="#fff" stroke-width="3"/></svg>
    <h4>Lorem Ipsum</h4>
    <p>Lorem ipsum dolor sit amet, consectetur adipiscing elit, sed do eiusmod tempor</p>
  </div>
</section>

<!-- doctor band -->
<section class="section doctor" role="img" aria-label="Darkened photo of a doctor in a white coat">
  <svg class="divider" style="top:66px" viewBox="0 0 80 20"><path d="M0 10h30M50 10h30" stroke="#8dc63f" stroke-width="1.5"/><circle cx="40" cy="10" r="6" fill="#8dc63f"/></svg>
  <h2 class="abs center">MEET OUR ARKANSAS MEDICAL DOCTOR</h2>
  <span class="btn" style="left:530px;top:191px;width:140px;height:38px;font-size:11px">Book Appointment</span>
</section>

<!-- network -->
<section class="section network">
  <svg class="divider" style="top:70px" viewBox="0 0 80 20"><path d="M0 10h30M50 10h30" stroke="#8dc63f" stroke-width="1.5"/><circle cx="40" cy="10" r="6" fill="#8dc63f"/></svg>
  <h2 class="abs center">Little Rock's First and Only Specialized Arkansas Medical Network</h2>
  <p class="abs intro">Lorem ipsum dolor sit amet, consectetur adipiscing elit, sed do eiusmod tempor incididunt ut labore et dolore magna aliqua. Ut enim ad minim veniam, quis nostrud exercitation ullamco laboris nisi.</p>
  <div class="card" style="left:150px">
    <div class="photo" role="img" aria-label="Photo of a cannabis plant close up" style="background:linear-gradient(135deg,#2f5a1d,#6fae3a 55%,#2a4a16)"></div>
    <h4>No Qualification? No Fee.</h4>
    <p>Lorem ipsum dolor sit amet, consectetur adipiscing elit, sed do eiusmod tempor incididunt</p>
  </div>
  <div class="card" style="left:462px">
    <div class="photo" role="img" aria-label="Photo of cannabis leaves on a dark background" style="background:linear-gradient(135deg,#1f3a12,#5c9a2a 50%,#1c2a12)"></div>
    <h4>No Qualification? No Fee.</h4>
    <p>Lorem ipsum dolor sit amet, consectetur adipiscing elit, sed do eiusmod tempor incididunt</p>
  </div>
  <div class="card" style="left:773px">
    <div class="photo" role="img" aria-label="Photo of a hand touching cannabis leaves" style="background:linear-gradient(135deg,#8bbf5a,#5c9a2d 50%,#a7c98a)"></div>
    <h4>No Qualification? No Fee.</h4>
    <p>Lorem ipsum dolor sit amet, consectetur adipiscing elit, sed do eiusmod tempor incididunt</p>
  </div>
</section>

<!-- subscribe -->
<section class="section subscribe">
  <div class="abs field">Your Email Address</div>
  <span class="btn">Subscribe</span>
  <span class="abs follow">Follow Us-</span>
  <span class="social" style="left:798px"></span>
  <span class="social" style="left:842px"></span>
  <span class="social" style="left:891px"></span>
</section>

<!-- footer -->
<footer class="section footer">
  <div class="brand">
    <span class="brand-mark"></span>
    <span class="brand-name" style="color:#fff;border-color:#fff">Bluecrest<br>Wellness<br>Group</span>
  </div>
  <p class="abs about-text">Neque porro quisquam est qui dolorem ipsum quia dolor sit amet, consectetur, adipisci velit.</p>
  <h4 style="left:563px">Quick Links</h4>
  <ul class="links">
    <li>Home</li><li>About</li><li>Qualify</li><li>Appointments</li><li>FAQ</li><li>News</li><li>Contact</li>
  </ul>
  <h4 style="left:776px">Contact Us</h4>
  <div class="contact" style="top:117px">
    <svg width="18" height="22" viewBox="0 0 18 22"><path d="M9 0a8 8 0 0 0-8 8c0 6 8 14 8 14s8-8 8-14a8 8 0 0 0-8-8z" fill="#fff"/><circle cx="9" cy="8" r="3" fill="#262626"/></svg>
    <span>123 Lorem Ipsum New York City</span>
  </div>
  <div class="contact" style="top:172px">
    <svg width="20" height="15" viewBox="0 0 24 18"><rect x="0" y="0" width="24" height="18" rx="2" fill="#fff"/><path d="M1 1l11 9 11-9" fill="none" stroke="#262626" stroke-width="2"/></svg>
    <span>Support@yourmail.com</span>
  </div>
  <div class="contact" style="top:232px">
    <svg width="20" height="20" viewBox="0 0 24 24"><path fill="#fff" d="M6.6 10.8a15 15 0 0 0 6.6 6.6l2.2-2.2c.3-.3.7-.4 1-.2 1.1.4 2.3.6 3.6.6.6 0 1 .4 1 1V20c0 .6-.4 1-1 1A17 17 0 0 1 3 4c0-.6.4-1 1-1h3.5c.6 0 1 .4 1 1 0 1.3.2 2.5.6 3.6.1.3 0 .7-.2 1z"/></svg>
    <span>88-888-8888</span>
  </div>
</footer>
<div class="section copyright">Copyright © 1998-2019 Pinefield Studio</div>

</body>
</html>
```